Tall Gum Equipment Hire Business Card Design

Tall Gum Equipment Hire Pty Ltd

WET or DRY HIRE

Kestrel M5-8 + attachments
Turf Cutter
Lawn mowers with catchers
Brushcutters
Blowers

We require a business card with the above information for a new equipment hire Company. Would like to see a redish/brown background or something to do with an Australian Tall Gum (Cattle Dog) on the business card as our Logo - even some sort of watermark as a background.

Industry/Entity Type

Business

Contact Information for Business Card

ABN: 81 207 935 316
17B Moller Road Emerald Qld 4720
PO Box 8157 Emerald Qld 4720
PH: 0413072846 or 0437150928
Email: sunvale.turf@quollnet.example

```html
<!DOCTYPE html>
<html lang="en">
<head>
<meta charset="utf-8">
<title>Tall Gum Equipment Hire – Business Card</title>
<link rel="stylesheet" href="https://fonts.googleapis.com/css2?family=Cabin:ital,wght@0,400;0,700;1,400&display=swap">
<style>
  :root {
    --orange: #e3803b;
    --orange-deep: #d0652b;
    --black: #000000;
    --ink: #111111;
    --white: #ffffff;
  }
  html, body {
    margin: 0;
    padding: 0;
    overflow: hidden;
    background: var(--white);
  }
  .card {
    position: relative;
    width: 1200px;
    height: 693px;
    overflow: hidden;
    background: var(--orange);
    font-family: "Cabin", sans-serif;
    color: var(--ink);
  }
  .watermark {
    position: absolute;
    left: 60px;
    top: 60px;
    width: 760px;
    height: 633px;
    background: radial-gradient(ellipse 55% 60% at 45% 55%, var(--orange-deep) 0%, rgba(208,101,43,0.55) 55%, rgba(208,101,43,0) 100%);
  }
  .side-panel {
    position: absolute;
    left: 926px;
    top: 0;
    width: 274px;
    height: 693px;
    background: var(--black);
  }
  .bracket {
    position: absolute;
    left: 926px;
    top: 54px;
  }
  .abn {
    position: absolute;
    left: 59px;
    top: 40px;
    font-size: 19px;
    font-style: italic;
    margin: 0;
  }
  .brand {
    position: absolute;
    left: 520px;
    top: 125px;
    margin: 0;
    font-weight: 700;
  }
  .brand-name {
    display: block;
    font-size: 88px;
    line-height: 1;
    letter-spacing: 1px;
  }
  .brand-sub {
    display: block;
    font-size: 32px;
    font-weight: 400;
    margin-top: 6px;
    letter-spacing: 0.5px;
  }
  .services {
    position: absolute;
    left: 59px;
    top: 410px;
    margin: 0;
    padding: 0;
    list-style: none;
    font-size: 29px;
    text-transform: uppercase;
  }
  .services li {
    height: 79px;
  }
  .sep {
    margin: 0 8px;
  }
  .contact {
    position: absolute;
    left: 926px;
    top: 385px;
    width: 274px;
    text-align: center;
    color: var(--white);
    font-style: italic;
  }
  .address {
    font-size: 20px;
    line-height: 27px;
    margin: 0;
    font-style: italic;
  }
  .phones {
    font-size: 30px;
    line-height: 44px;
    margin: 28px 0 0;
    letter-spacing: 1px;
  }
  .email {
    font-size: 16px;
    margin: 2px 0 0;
  }
</style>
</head>
<body>
<div class="card">
  <div class="watermark" role="img" aria-label="Faint background watermark of the company's cattle dog emblem"></div>

  <div class="side-panel"></div>
  <svg class="bracket" width="180" height="290" viewBox="0 0 180 290" aria-hidden="true">
    <rect x="0" y="0" width="178" height="287" fill="var(--orange)"/>
    <rect x="0" y="25" width="161" height="243" fill="var(--black)"/>
    <rect x="0" y="63" width="141" height="166" fill="var(--orange)"/>
  </svg>

  <p class="abn">ABN: 81 207 935 316</p>

  <h1 class="brand">
    <span class="brand-name">TALL GUM</span>
    <span class="brand-sub">EQUIPMENT HIRE PTY LTD</span>
  </h1>

  <ul class="services">
    <li>Wet or Dry Hire<span class="sep">|</span>Kestrel M5-8 + Attachments</li>
    <li>Turf Cutter<span class="sep">|</span>Lawn Mowers with Catchers</li>
    <li>Brushcutters<span class="sep">|</span>Blowers</li>
  </ul>

  <address class="contact">
    <p class="address">17B Moller Road<br>Emerald<br>Qld 4720<br>PO Box 8157</p>
    <p class="phones">0413072846<br>0437150928</p>
    <p class="email">sunvale.turf@quollnet.example</p>
  </address>
</div>
</body>
</html>
```